ORVAN LOGIC LTD

See website just wanted it updated and more fresh ; https://www.orvan-logic.co.uk

Coding

Coded - Design and coding required

Colors

Designer to choose colors to be used in the design.

```html
<!DOCTYPE html>
<html lang="en">
<head>
<meta charset="utf-8">
<title>Orvan Logic Ltd</title>
<link href="https://fonts.googleapis.com/css2?family=Signika:wght@400;500;600&family=Open+Sans:ital,wght@0,400;0,600;0,700;1,400&display=swap" rel="stylesheet">
<style>
:root{
  --orange:#f26a25;
  --blue:#0a6fc2;
  --ink:#333333;
  --text:#666666;
  --line:#e3e3e3;
  --white:#ffffff;
  --footer:#1e2a30;
  --head:'Signika',sans-serif;
  --body:'Open Sans',sans-serif;
}
*{box-sizing:border-box;margin:0;padding:0}
html,body{width:1200px;height:3120px;overflow:hidden;background:var(--white)}
body{font-family:var(--body);color:var(--text);position:relative}
.wrap{width:878px;margin:0 auto;position:relative}
.btn{display:inline-block;background:var(--orange);color:var(--white);font-family:var(--body);font-weight:700;font-size:13px;border-radius:3px;text-align:center;line-height:45px;width:150px;text-decoration:none}

/* top bar */
.topbar{height:75px;border-bottom:1px solid var(--line)}
.topbar .wrap{height:75px;display:flex;align-items:center;justify-content:space-between}
.contact-chip{display:flex;align-items:center;gap:14px;font-size:13px;color:#555}
.chip-icon{width:34px;height:34px;border:1.5px solid var(--orange);border-radius:4px;display:flex;align-items:center;justify-content:center}
.brand{display:flex;align-items:center;gap:8px;font-family:var(--head);font-weight:600;font-size:28px;color:var(--blue)}
.brand-mark{width:14px;height:14px;background:var(--orange)}

/* nav */
.mainnav{height:60px;display:flex;align-items:center;justify-content:center;gap:26px;font-size:12.5px;color:#444;border-bottom:1px solid #f0f0f0}

/* hero */
.hero{height:562px;position:relative;background:linear-gradient(#e9e9e9,#dcdcdc 60%,#b9a48e);text-align:center;overflow:hidden}
.hero-photo{position:absolute;inset:0;background:linear-gradient(180deg,#ececec 0%,#e2e2e2 45%,#c8b8a3 75%,#8a8a7c 100%)}
.hero-copy{position:relative;padding-top:60px}
.hero h1{font-family:var(--head);font-weight:500;font-size:35px;line-height:45px;color:var(--ink)}
.hero p{font-size:12.5px;line-height:22px;color:#666;width:470px;margin:12px auto 16px}

/* about */
.about{height:352px;position:relative;text-align:center}
.about-map{position:absolute;left:182px;top:10px;width:380px;height:300px;border-radius:45% 55% 40% 60%;background:radial-gradient(circle,#eeeeee 0%,#f7f7f7 60%,transparent 75%)}
.about-copy{position:relative;padding-top:72px}
.eyebrow{font-family:var(--head);font-weight:600;font-size:23px;color:var(--blue);letter-spacing:.5px}
.about h2,.section-title{font-family:var(--head);font-weight:500;font-size:35px;line-height:45px;color:var(--ink)}
.about p{font-size:12.5px;line-height:22px;width:470px;margin:14px auto 18px}

/* services */
.services{height:560px;text-align:center;padding-top:78px}
.services .lead{font-size:12.5px;line-height:22px;width:410px;margin:10px auto 20px}
.cards{display:flex;justify-content:space-between}
.card{width:278px;height:341px;box-shadow:0 0 8px rgba(0,0,0,.12);padding:6px;position:relative}
.card-photo{height:172px;position:relative}
.photo-a{background:linear-gradient(135deg,#5a6678,#9aa6b4 50%,#3d4756)}
.photo-b{background:linear-gradient(135deg,#c9c4ba,#8a8378 55%,#3d3a35)}
.photo-c{background:linear-gradient(135deg,#3f6a8c,#8db4d2 55%,#2f5674)}
.card-badge{position:absolute;right:8px;bottom:-22px;width:44px;height:44px;background:var(--orange);border-radius:4px;display:flex;align-items:center;justify-content:center}
.card h3{font-family:var(--head);font-weight:400;font-size:17px;color:var(--blue);margin:22px 0 10px}
.card p{font-size:12.3px;line-height:22.5px;padding:0 6px}

/* testimonial */
.testimonial{height:450px;position:relative;text-align:center;color:var(--white);overflow:hidden}
.testimonial-photo{position:absolute;inset:0;background:linear-gradient(90deg,#4a4c4a,#6b6a5f 30%,#5b6675 60%,#4d5357)}
.testimonial-shade{position:absolute;inset:0;background:rgba(30,34,40,.45)}
.testimonial-copy{position:relative;padding-top:58px}
.testimonial h2{font-family:var(--head);font-weight:500;font-size:35px}
.quote{font-style:italic;font-size:11.8px;line-height:22.5px;width:610px;margin:22px auto 18px}
.cite{color:var(--orange);font-size:13.5px;line-height:22.5px;font-weight:600}
.divider{width:38px;height:1px;background:rgba(255,255,255,.6);margin:26px auto 0}
.pager{display:flex;justify-content:center;align-items:flex-end;gap:24px;margin-top:38px;font-family:var(--head);font-weight:600}
.pager span{font-size:14px}
.pager .on{font-size:19px;margin-bottom:10px}

/* contact */
.contact{height:488px;text-align:center;padding-top:78px}
.form{width:645px;margin:26px auto 0;text-align:left}
.row{display:flex;justify-content:space-between;margin-bottom:23px}
.field{height:37px;border:1px solid #cfcfcf;font-size:11.5px;color:#888;padding:11px 9px}
.half{width:300px}
.full{width:645px}
.tall{height:74px;margin-bottom:25px}
.form .btn{display:block;margin:0 auto}

/* ask */
.ask{position:absolute;left:300px;top:2561px;width:600px;height:158px;background:var(--white);border-radius:80px;text-align:center;z-index:2;padding-top:22px}
.ask h2{font-family:var(--head);font-weight:400;font-size:30px;color:var(--ink)}
.ask p{font-size:12.3px;line-height:22.5px;width:480px;margin:10px auto 6px}
.ask a{color:var(--orange);font-weight:700;font-size:13px}

/* footer */
.footer{position:absolute;left:0;top:2669px;width:1200px;height:451px;overflow:hidden;color:#ddd}
.footer-photo{position:absolute;inset:0;background:linear-gradient(100deg,#1b2428 0%,#233036 55%,#3a3a2e 80%,#4a3b2c 100%)}
.footer-inner{position:relative}
.footer .brand{justify-content:center;color:#e0e0e0;margin-top:76px}
.cols{display:flex;width:878px;margin:42px auto 0}
.col h4{font-family:var(--head);font-weight:400;font-size:22px;color:var(--white);margin-bottom:22px}
.col-contact{width:265px}
.col-hours{width:273px}
.col-links{width:239px}
.info{display:flex;gap:16px;font-size:12px;line-height:22px;margin-bottom:14px;align-items:flex-start}
.list{list-style:none;font-size:12px}
.list li{display:flex;align-items:center;gap:10px;line-height:28px}
.list li::before{content:"";width:4px;height:4px;background:#fff;transform:rotate(45deg)}
.hours li{line-height:33px;font-size:12px}
.hours b{color:var(--orange);font-weight:400;font-size:14px;margin-right:4px}
.copyright{position:absolute;left:0;right:0;bottom:0;height:37px;border-top:1px solid rgba(255,255,255,.2);text-align:center;font-size:11px;line-height:37px;color:#ddd}
</style>
</head>
<body>

<header class="topbar">
  <div class="wrap">
    <div class="contact-chip">
      <span class="chip-icon"><svg width="16" height="16" viewBox="0 0 24 24"><path fill="#0a6fc2" d="M6.6 10.8a15.1 15.1 0 0 0 6.6 6.6l2.2-2.2a1 1 0 0 1 1-.25 11.4 11.4 0 0 0 3.6.57 1 1 0 0 1 1 1V20a1 1 0 0 1-1 1A17 17 0 0 1 3 4a1 1 0 0 1 1-1h3.5a1 1 0 0 1 1 1c0 1.25.2 2.45.57 3.57a1 1 0 0 1-.25 1z"/></svg></span>
      0161 480 3926
    </div>
    <div class="brand"><span class="brand-mark"></span>Orvan Logic</div>
    <div class="contact-chip">
      <span class="chip-icon"><svg width="18" height="14" viewBox="0 0 18 14"><rect x="1" y="1" width="16" height="12" rx="1" fill="#0a6fc2"/><path d="M1.5 2 9 8l7.5-6" stroke="#fff" stroke-width="1.5" fill="none"/></svg></span>
      info@orvan-logic.co.uk
    </div>
  </div>
</header>

<nav class="mainnav">
  <span>Home</span><span>Services</span><span>About Us</span><span>Helpdesk</span><span>Contact Us</span>
  <svg width="16" height="16" viewBox="0 0 16 16"><circle cx="6.5" cy="6.5" r="5" stroke="#888" stroke-width="1.4" fill="none"/><path d="m10.2 10.2 4.5 4.5" stroke="#888" stroke-width="1.4"/></svg>
</nav>

<section class="hero">
  <div class="hero-photo" role="img" aria-label="Group of smiling students sitting against a white brick wall"></div>
  <div class="hero-copy">
    <h1>Education, Support and<br>Installation of All Technologies</h1>
    <p>Lorem Ipsum is simply dummy text of the printing and typesetting industry. Lorem Ipsum has been the industry's standard dummy text ever since the 1500s.</p>
    <a class="btn">Learn More</a>
  </div>
</section>

<section class="about">
  <div class="about-map" role="img" aria-label="Faint dotted world map decoration"></div>
  <div class="about-copy">
    <div class="eyebrow">ABOUT US</div>
    <h2>Complete Primary and Secondary<br>School Support</h2>
    <p>We offer support in all aspects of ICT in education, from technical faults to assisting teachers and coordinators to meet the requirements of the computing curriculum</p>
    <a class="btn">Find Out More</a>
  </div>
</section>

<section class="services">
  <div class="wrap">
    <h2 class="section-title">Services</h2>
    <p class="lead">We provide a range of services, each service will be tailored to meet the individual needs of each school.</p>
    <div class="cards">
      <article class="card">
        <div class="card-photo photo-a" role="img" aria-label="Technicians working in a server room">
          <span class="card-badge"><svg width="24" height="24" viewBox="0 0 24 24" fill="none" stroke="#fff" stroke-width="1.6"><path d="M4 20 14 10M14 10l3-6 3 3-6 3M20 20 9 9M9 9 4 4"/></svg></span>
        </div>
        <h3>ICT Support</h3>
        <p>We provide a wide range of ICT support packages, which all include regular onsite visits, telephone, email and helpdesk support plus secure remote assistance.</p>
      </article>
      <article class="card">
        <div class="card-photo photo-b" role="img" aria-label="Person working at a laptop on a desk">
          <span class="card-badge"><svg width="26" height="22" viewBox="0 0 26 22" fill="none" stroke="#fff" stroke-width="1.6"><rect x="4" y="3" width="18" height="12" rx="1"/><path d="M1 18h24"/></svg></span>
        </div>
        <h3>Hardware Sales</h3>
        <p>We supply and install hardware from the world's leading manufacturers including: Veltra, Koruma, Axen, Brightline, Novique and many more.</p>
      </article>
      <article class="card">
        <div class="card-photo photo-c" role="img" aria-label="Hand touching a cloud computing interface">
          <span class="card-badge"><svg width="26" height="22" viewBox="0 0 26 22" fill="none" stroke="#fff" stroke-width="1.6"><path d="M7 16a5 5 0 0 1 0-10 7 7 0 0 1 13 2 4 4 0 0 1-1 8z"/><rect x="10" y="10" width="6" height="8"/></svg></span>
        </div>
        <h3>Cloud &amp; Hosting Services</h3>
        <p>We offer an extensive range of cloud and hosting services including websites, domains, blogs, emails and cloud storage solutions.</p>
      </article>
    </div>
  </div>
</section>

<section class="testimonial">
  <div class="testimonial-photo" role="img" aria-label="Smiling school children with backpacks"></div>
  <div class="testimonial-shade"></div>
  <div class="testimonial-copy">
    <h2>What Our Customers Say About Us</h2>
    <p class="quote">“Orvan Logic Ltd is extremely competitive price wise and is flexible with their working hours. Regardless of the size of job, the company are always happy to help. Our technician, Tom, has been with us for over 2 years and is very hard working and committed to ensuring we get the best possible support he can offer. I enjoy working with Orvan Logic and would have no hesitation in recommending them to other schools or businesses.”</p>
    <p class="cite">Maria Pennock-Hale, Headteacher at Westbrook Lane<br>Junior School</p>
    <div class="divider"></div>
    <div class="pager"><span>01</span><span class="on">02</span><span>03</span></div>
  </div>
</section>

<section class="contact">
  <h2 class="section-title">Contact Us</h2>
  <div class="form">
    <div class="row"><div class="field half">Your Name</div><div class="field half">Your E-mail</div></div>
    <div class="row"><div class="field full">Subject</div></div>
    <div class="field full tall">Your Message</div>
    <a class="btn">SEND</a>
  </div>
</section>

<div class="ask">
  <h2>Ask us anything</h2>
  <p>Whether you have got a quick question or want to run through the details of your next big project, we can help. speack to one of our experts.</p>
  <a>Send Us a Message</a>
</div>

<footer class="footer">
  <div class="footer-photo" role="img" aria-label="Dark desk scene with coloured pencils in a holder and stacked books"></div>
  <div class="footer-inner">
    <div class="brand"><span class="brand-mark"></span>Orvan Logic</div>
    <div class="cols">
      <div class="col col-contact">
        <h4>Contact Orvan-Logic</h4>
        <div class="info"><svg width="18" height="24" viewBox="0 0 18 24"><path fill="#f26a25" d="M9 0a9 9 0 0 0-9 9c0 7 9 15 9 15s9-8 9-15a9 9 0 0 0-9-9z"/><circle cx="9" cy="9" r="3.5" fill="#1e2a30"/></svg><span>Halden Court, Marlow Street<br>Ashby Lancashire AL4 7QR</span></div>
        <div class="info"><svg width="18" height="18" viewBox="0 0 24 24"><path fill="#f26a25" d="M6.6 10.8a15.1 15.1 0 0 0 6.6 6.6l2.2-2.2a1 1 0 0 1 1-.25 11.4 11.4 0 0 0 3.6.57 1 1 0 0 1 1 1V20a1 1 0 0 1-1 1A17 17 0 0 1 3 4a1 1 0 0 1 1-1h3.5a1 1 0 0 1 1 1c0 1.25.2 2.45.57 3.57a1 1 0 0 1-.25 1z"/></svg><span>0161 480 3926</span></div>
        <div class="info"><svg width="18" height="14" viewBox="0 0 18 14"><rect x="0" y="1" width="18" height="12" fill="#f26a25"/><path d="M0.5 2 9 8l8.5-6" stroke="#1e2a30" stroke-width="1.5" fill="none"/></svg><span>info@orvan-logic.co.uk</span></div>
      </div>
      <div class="col col-hours">
        <h4>Opening Hours</h4>
        <ul class="list hours">
          <li><b>Monday-Friday:</b>8am-6pm</li>
          <li><b>Saturday:</b>8am-4pm</li>
          <li><b>Sunday:</b>8am-6pm</li>
        </ul>
      </div>
      <div class="col col-links">
        <h4>Quick Links</h4>
        <ul class="list"><li>Home</li><li>Services</li><li>About us</li><li>Helpdesk</li><li>Contact Us</li></ul>
      </div>
      <div class="col">
        <h4>Follow Us</h4>
        <ul class="list"><li>Friendwall</li><li>Chirpline</li><li>Careerlink</li><li>Photoloop</li></ul>
      </div>
    </div>
  </div>
  <div class="copyright">©Orvan Logic Ltd - 2020 All Rights Reserved.</div>
</footer>

</body>
</html>
```